Biotech company needs graphics to describe company culture

We would like to have help in describing our company culture in a graphic way.Our "local culture" focus areas (Proud & Accountable, Challenge & Collaborate) builds on the Corvane Halbrook corporate values which is Integrity, Intensity, Innovation and Involvement. Our "local norms" is describing behaviours which we want to see more of, and that will ensure that we get better at our culture focus. We would like this to be expressed in a graphic way, getting an image we can use for multiple purposes in a format that fits into PowerPoint slides, can be printed on mousepads etc. We want one Norwegian and one English version. Attached is an example of the desired content in both languages.

Target Market(s)

Employees

Industry/Entity Type

Biotechnology

Font styles to use
Serif

Colors

Designer to choose colors to be used in the design.

Requirements
Nice to have
• Want the employees to intuitive understand the connection from values to cultural focus to norms. The norms are the most important to highlight to our employees. They should understand that if they do more of the desired behaviours (norms), then they will have act according to our culture focus and our values.

```html
<!DOCTYPE html>
<html lang="en">
<head>
<meta charset="utf-8">
<title>Culture Focus – Corvane Halbrook</title>
<link rel="stylesheet" href="https://fonts.googleapis.com/css2?family=Roboto+Condensed:wght@400;500;700&display=swap">
<style>
  :root {
    --bg-light: #dfe6e1;
    --bg-mid: #c7d6cc;
    --bg-deep: #a9c0b2;
    --bg-seam: #d3ddd6;
    --ink: #1f1f1f;
    --ink-soft: #3a3d3c;
    --accent: #e3262f;
    --white: #ffffff;
  }
  * { margin: 0; padding: 0; box-sizing: border-box; }
  html, body { width: 1200px; height: 675px; overflow: hidden; background: var(--bg-light); }
  body { font-family: "Roboto Condensed", "Arial Narrow", sans-serif; color: var(--ink); }
  .canvas { position: relative; width: 1200px; height: 675px; overflow: hidden; background: var(--bg-light); }
  .backdrop { position: absolute; inset: 0; }

  .scene { position: absolute; border-radius: 6px; opacity: .9; }
  .scene-team-desk { left: 20px; top: 80px; width: 370px; height: 220px;
    background: linear-gradient(160deg, #9aa39e, #5f6562 60%, #cf7d71); }
  .scene-pair-review { left: 900px; top: 105px; width: 255px; height: 275px;
    background: linear-gradient(200deg, #a6aca9, #6b716e); border-radius: 50% 50% 12px 12px; }
  .scene-team-console { left: 62px; top: 370px; width: 420px; height: 245px;
    background: linear-gradient(170deg, #8d9490, #4f5552 70%); }

  .connector { position: absolute; height: 0; border-top: 2px dotted var(--accent); }
  .norm {
    position: absolute; background: var(--white);
    border-bottom: 2px solid var(--accent);
    box-shadow: 0 2px 6px rgba(0,0,0,.12);
    font-size: 23px; font-weight: 500; line-height: 1.5; letter-spacing: -.2px;
    padding: 10px 14px;
  }
  .norm em { font-style: normal; color: var(--accent); }
  .norm::before {
    content: ""; position: absolute; left: -6px; top: 4px; width: 11px; height: 11px;
    background: var(--accent);
  }
  .norm-ownership { left: 402px; top: 134px; width: 423px; height: 89px; }
  .norm-feedback { left: 466px; top: 300px; width: 415px; height: 56px; }
  .norm-curious { left: 537px; top: 429px; width: 438px; height: 90px; }

  .label { position: absolute; display: flex; align-items: center; gap: 10px; }
  .label-mark { width: 10px; height: 10px; background: var(--accent); }
  .label-bar {
    background: var(--ink); color: var(--white);
    font-size: 13px; letter-spacing: 2.5px; font-weight: 500;
    padding: 2px 16px; text-transform: uppercase; line-height: 16px;
  }
  .culture-label { left: 545px; top: 35px; }
  .values-label { left: 545px; top: 600px; }

  .chain { position: absolute; color: var(--accent); font-size: 17px; font-weight: 500; display: flex; gap: 8px; align-items: center; }
  .chain .arrow { color: var(--ink); font-size: 10px; }
  .focus-chain { left: 549px; top: 64px; }
  .values-chain { left: 550px; top: 628px; gap: 6px; }
  .values-chain .sep { color: var(--ink); }

  .brand {
    position: absolute; left: 922px; top: 604px;
    display: flex; align-items: center; gap: 10px;
    font-size: 28px; font-weight: 500; color: var(--ink-soft); letter-spacing: 0;
  }
  .brand-mark { width: 14px; height: 14px; background: var(--ink-soft); }
</style>
</head>
<body>
<main class="canvas">
  <svg class="backdrop" width="1200" height="675" viewBox="0 0 1200 675" aria-hidden="true">
    <rect width="1200" height="675" fill="var(--bg-light)"/>
    <polygon points="0,0 487,0 412,675 0,675" fill="var(--bg-mid)"/>
    <polygon points="0,288 440,420 412,675 0,675" fill="var(--bg-deep)"/>
    <polygon points="487,0 412,675 432,675 507,0" fill="var(--bg-seam)"/>
  </svg>

  <div class="scene scene-team-desk" role="img" aria-label="Illustration of three colleagues gathered around a laptop at a desk"></div>
  <div class="scene scene-pair-review" role="img" aria-label="Illustration of two colleagues reviewing documents together"></div>
  <div class="scene scene-team-console" role="img" aria-label="Illustration of three colleagues discussing around a control console"></div>

  <div class="label culture-label">
    <span class="label-mark" aria-hidden="true"></span>
    <span class="label-bar">Culture Focus</span>
  </div>
  <p class="chain focus-chain">
    <span>Proud</span><span class="arrow">▶</span>
    <span>Accountable</span><span class="arrow">▶</span>
    <span>Challenge</span><span class="arrow">▶</span>
    <span>Collaborate</span><span class="arrow">▶</span>
  </p>

  <span class="connector" style="left:338px; top:141px; width:58px;"></span>
  <p class="norm norm-ownership">I take ownership, am <em>solution-oriented</em><br>and ensure implementation</p>

  <span class="connector" style="left:886px; top:310px; width:46px;"></span>
  <p class="norm norm-feedback">I give and seek <em>constructive feedback</em></p>

  <span class="connector" style="left:462px; top:438px; width:68px;"></span>
  <p class="norm norm-curious">I am curious about others’ perspectives<br>and <em>new ways</em> of doing things</p>

  <div class="label values-label">
    <span class="label-mark" aria-hidden="true"></span>
    <span class="label-bar">Our Values</span>
  </div>
  <p class="chain values-chain">
    <span>Integrity</span><span class="sep">|</span>
    <span>Intensity</span><span class="sep">|</span>
    <span>Innovation</span><span class="sep">|</span>
    <span>Involvement</span>
  </p>

  <p class="brand"><span class="brand-mark" aria-hidden="true"></span>Corvane Halbrook</p>
</main>
</body>
</html>
```